10 Page Marketing Report Template - Cindermoor Care Allies

https://www.vidquill.example/share/7f1e9c04b2d84a61a5c3e9d02b6f4a17

We are creating a professional, modern, and slightly edgy PDF-style report document (about 10 pages) to showcase the results of a client’s first 30 days with Cindermoor Care Allies.

The report will be designed as a customizable Plakkit template so the Client Success team can easily update logos, screenshots, and text for each client.

This document will serve as both a visual presentation piece and a report deliverable, blending clean design, modern layout, and data-driven storytelling.

I am attaching the content for the report doc and the design brief along with the logo.
Here is our website for design style, look, and feel: https://cindermoorcare.example/

Here is a quick overview video I made:

```html
<!DOCTYPE html>
<html lang="en">
<head>
<meta charset="utf-8">
<title>30 Days to Value Report – Cindermoor Care Allies</title>
<link href="https://fonts.googleapis.com/css2?family=Montserrat:wght@400;500;600;700&family=Open+Sans:wght@700&display=swap" rel="stylesheet">
<style>
:root{
  --brand-blue:#0e3e91;
  --ink:#111111;
  --panel-gray:#f3f3f3;
  --white:#ffffff;
  --rule-green:#3aa86b;
}
*{margin:0;padding:0;box-sizing:border-box}
html,body{width:1200px;height:1200px;overflow:hidden;background:var(--white)}
body{position:relative;font-family:'Montserrat',sans-serif;color:var(--ink)}
.page{position:absolute}
ul{list-style:none}
li{position:relative;padding-left:10px}
li::before{content:"";position:absolute;left:0;top:0.55em;width:3px;height:3px;border-radius:50%;background:currentColor}

/* Cover */
.cover{left:0;top:0;width:576px;height:261px;background:var(--brand-blue);color:var(--white)}
.cover__brand{position:absolute;left:450px;top:14px;width:109px;height:73px;background:var(--white);display:flex;align-items:center;justify-content:center;gap:5px;padding:0 6px}
.cover__brand-mark{width:8px;height:8px;background:var(--brand-blue);flex:none}
.cover__brand-name{font-size:8.5px;font-weight:600;color:var(--ink);line-height:1.2;text-transform:uppercase}
.cover__title{position:absolute;left:0;width:524px;top:131px;text-align:center;font-size:25px;font-weight:700}
.cover__meta{position:absolute;left:0;width:560px;top:170px;text-align:center;font-size:11.6px;line-height:15.6px;font-weight:400}

/* Audits */
.audits{left:606px;top:0;width:594px;height:438px}
.audits__title{position:absolute;left:0;width:560px;top:12px;text-align:center;color:var(--brand-blue);font-size:25px;font-weight:700;line-height:34px}
.audits__intro{position:absolute;left:8px;width:586px;top:89px;text-align:center;font-size:11px;line-height:16px}
.audits__heading{position:absolute;left:17px;top:148px;font-family:'Open Sans',sans-serif;font-weight:700;font-size:14.5px}
.audits__list{position:absolute;font-size:9.3px;line-height:13px}
.audits__list--left{left:26px;top:174px;width:232px}
.audits__list--left li{text-align:center;padding-left:12px}
.audits__list--right{left:316px;top:181px;width:278px}

/* Welcome */
.welcome{left:0;top:438px;width:576px;height:350px}
.welcome__title{position:absolute;left:0;width:530px;top:16px;text-align:center;font-size:24px;font-weight:700}
.welcome__rule{position:absolute;left:99px;top:60px;width:338px;height:1px;background:var(--rule-green)}
.welcome__body{position:absolute;left:14px;width:548px;top:80px;text-align:center;font-size:10.2px;line-height:13.8px}
.welcome__body p+p{margin-top:14px}

/* Website progress */
.progress{left:606px;top:438px;width:594px;height:337px;background:var(--panel-gray)}
.progress__title{position:absolute;left:34px;top:17px;color:var(--brand-blue);font-size:25px;font-weight:700}
.progress__launched{position:absolute;left:34px;top:59px;font-size:12.3px;font-weight:700}
.progress__label{position:absolute;left:34px;font-size:9.8px;font-weight:700}
.progress__list{position:absolute;left:42px;font-size:9.8px;line-height:13px}
.progress__list li{padding-left:10px}

/* Highlights */
.highlights{left:0;top:820px;width:576px;height:323px;background:var(--panel-gray)}
.highlights__title{position:absolute;left:30px;top:16px;color:var(--brand-blue);font-size:25px;font-weight:700}
.highlights__list{position:absolute;left:29px;top:71px;font-size:14px;line-height:18px}
.highlights__list li{padding-left:11px}
.highlights__list li::before{width:4px;height:4px;top:0.5em}
.highlights__list li::before,.partner-profile__list li::before{background:var(--brand-blue)}

/* Business profile */
.partner-profile{left:606px;top:820px;width:594px;height:323px}
.partner-profile__title{position:absolute;left:38px;top:16px;color:var(--brand-blue);font-size:25px;font-weight:700}
.partner-profile__list{position:absolute;left:48px;top:68px;font-size:11.8px;line-height:15.7px}
</style>
</head>
<body>

<section class="page cover">
  <div class="cover__brand">
    <span class="cover__brand-mark"></span>
    <span class="cover__brand-name">Cindermoor Care Allies</span>
  </div>
  <h1 class="cover__title">30 Days to Value Report</h1>
  <div class="cover__meta">
    <p>Client: [Client Name]</p>
    <p>Date: [Month / Year]</p>
    <p>Prepared by: Cindermoor Care Allies</p>
  </div>
</section>

<section class="page audits">
  <h2 class="audits__title">Comprehensive Audits &amp; Strategy<br>Development</h2>
  <p class="audits__intro">To ensure long-term results, our team conducted a full suite of technical and strategic audits during<br>the first month. These insights guided your SEO roadmap and content strategy moving forward.</p>
  <h3 class="audits__heading">Audits &amp; Deliverables Completed:</h3>
  <ul class="audits__list audits__list--left">
    <li>Technical SEO Audit: Site health, indexation,<br>and crawl efficiency</li>
    <li>Backlink Audit: Link quality, toxicity review,<br>and authority scoring</li>
    <li>Competitor Analysis: Top-ranking<br>competitors’ content, backlinks, and<br>keyword profiles</li>
    <li>On-Page SEO Audit: Metadata, headings,<br>internal links, and content structure</li>
  </ul>
  <ul class="audits__list audits__list--right">
    <li>Content Audit: Keyword targeting,<br>topical gaps, and conversion opportunities</li>
    <li>Strategy Development: 90-day SEO plan and keyword<br>roadmap created</li>
  </ul>
</section>

<section class="page welcome">
  <h2 class="welcome__title">Welcome &amp; Overview</h2>
  <div class="welcome__rule"></div>
  <div class="welcome__body">
    <p>The first 30 days are about creating momentum. Our goal was to build the foundation for measurable<br>growth — from your website and Wayfind Business Profile to your SEO systems, audits, and backlink<br>strategy.</p>
    <p>This report highlights what’s been accomplished and what’s next in your marketing journey.</p>
  </div>
</section>

<section class="page progress">
  <h2 class="progress__title">Website Progress</h2>
  <p class="progress__launched">Launched Pages: [List live pages: Home, About, Services, Contact]</p>
  <p class="progress__label" style="top:129px">Optimizations Completed:</p>
  <ul class="progress__list" style="top:151px">
    <li>On-page SEO (titles, meta, H1s)</li>
    <li>Local schema added</li>
    <li>Call tracking integrated</li>
    <li>Mobile responsiveness reviewed</li>
  </ul>
  <p class="progress__label" style="top:221px">Next Steps:</p>
  <ul class="progress__list" style="top:240px">
    <li>CRO improvements</li>
    <li>Additional service or location pages</li>
  </ul>
</section>

<section class="page highlights">
  <h2 class="highlights__title">Highlights &amp; Quick Wins</h2>
  <ul class="highlights__list">
    <li>Website launched and optimized for SEO</li>
    <li>Wayfind Business Profiles verified and optimized</li>
    <li>Comprehensive SEO audits completed</li>
    <li>Backlink strategy implementation underway</li>
    <li>First blog articles published</li>
    <li>Tracking and analytics systems connected</li>
  </ul>
</section>

<section class="page partner-profile">
  <h2 class="partner-profile__title">Wayfind Business Profile</h2>
  <ul class="partner-profile__list">
    <li>Profiles verified and optimized</li>
    <li>Categories, services, and photos updated</li>
    <li>Images optimized for visibility and engagement</li>
    <li>Review strategy initiated</li>
    <li>Visibility and engagement tracking started</li>
  </ul>
</section>

</body>
</html>
```